Real Estate Marketing Company Needs 1 Page 8.5x11 Price List Flyer Design

We need a 1 page 8.5in x 11in price list flyer that is intended for drop off at local offices. This is intended to show all the services we offer including pricing to potential new clients. It should be separated into sections for the different services we offer. I'd also like some photos and our Logo on the list to make it look nice so its not all text. Try to incorporate the logo colors in the design.

Industry/Entity Type

Real Estate

Requirements
Must have
• Price List
• Photos
• Logo
• website address

```html
<!DOCTYPE html>
<html lang="en">
<head>
<meta charset="utf-8">
<title>Open House Imaging – Price List</title>
<link href="https://fonts.googleapis.com/css2?family=Hind:wght@400;500&display=swap" rel="stylesheet">
<style>
  :root {
    --brand-red: #c0202a;
    --ink: #1d1d1d;
    --muted: #8a8a8a;
    --band-grey: #8c8c8c;
    --divider: #0c0c0c;
    --paper: #ffffff;
  }
  * { margin: 0; padding: 0; box-sizing: border-box; }
  html, body { width: 1200px; height: 771px; overflow: hidden; background: var(--paper); }
  body { font-family: "Hind", Arial, sans-serif; color: var(--ink); }
  .canvas { position: relative; width: 1200px; height: 771px; }
  .photo-grid { position: absolute; left: 0; top: 0; }
  .page-divider { position: absolute; left: 590px; top: 0; width: 9px; height: 771px; background: var(--divider); }

  .tagline { position: absolute; left: 300px; top: 82px; width: 212px; text-align: center;
    font-size: 22px; line-height: 29px; color: var(--muted); }

  .brand { position: absolute; display: flex; flex-direction: column; align-items: center; }
  .brand-mark { width: 60px; height: 60px; border-radius: 50%; background: var(--ink); }
  .brand-name { font-weight: 500; color: var(--ink); white-space: nowrap; letter-spacing: 0.5px; }
  .brand--cover { left: 335px; top: 458px; width: 170px; }
  .brand--cover .brand-mark { width: 72px; height: 72px; }
  .brand--cover .brand-name { margin-top: 10px; font-size: 20px; }

  .services-band { position: absolute; left: 0; top: 598px; width: 590px; height: 46px;
    background: var(--brand-red); color: var(--paper); font-size: 21px; font-weight: 500;
    text-align: center; line-height: 50px; }
  .cover-contact { position: absolute; left: 0; top: 674px; width: 590px; text-align: center;
    font-size: 15px; line-height: 21px; color: var(--muted); }

  .section-title { position: absolute; height: 28px; background: var(--brand-red); color: var(--paper);
    font-size: 14px; font-weight: 500; line-height: 31px; padding-left: 11px; letter-spacing: 0.3px; }
  .price-list { position: absolute; list-style: none; font-size: 12.5px; line-height: 16.1px; color: var(--ink); }

  .title-packages { left: 635px; top: 38px; width: 358px; }
  .list-packages { left: 635px; top: 73px; }
  .title-floorplans { left: 880px; top: 139px; width: 276px; }
  .list-floorplans { left: 880px; top: 175px; width: 300px; }
  .title-photo { left: 990px; top: 334px; width: 166px; }
  .list-photo { left: 990px; top: 370px; }
  .title-extra { left: 840px; top: 469px; width: 316px; }
  .list-extra { left: 840px; top: 505px; width: 340px; }

  .booking-band { position: absolute; left: 600px; top: 645px; width: 600px; height: 65px;
    background: var(--band-grey); }
  .booking-text { position: absolute; left: 805px; top: 655px; width: 390px; text-align: center;
    color: var(--paper); font-size: 12.5px; line-height: 15.5px; }
  .brand-box { position: absolute; left: 644px; top: 621px; width: 157px; height: 107px;
    background: var(--paper); border: 2px solid var(--brand-red); }
  .brand--back { left: 0; top: 12px; width: 153px; }
  .brand--back .brand-mark { width: 52px; height: 52px; }
  .brand--back .brand-name { margin-top: 8px; font-size: 14px; }
</style>
</head>
<body>
<main class="canvas">
  <svg class="photo-grid" width="1200" height="771" viewBox="0 0 1200 771">
    <defs>
      <linearGradient id="tone-interior" x1="0" y1="0" x2="0" y2="1">
        <stop offset="0" stop-color="#d9d2c6"/><stop offset="1" stop-color="#7e5c43"/>
      </linearGradient>
      <linearGradient id="tone-pool" x1="0" y1="0" x2="0" y2="1">
        <stop offset="0" stop-color="#4f7a3a"/><stop offset="0.6" stop-color="#5fb3d4"/><stop offset="1" stop-color="#c98a7c"/>
      </linearGradient>
      <linearGradient id="tone-aerial" x1="0" y1="0" x2="0" y2="1">
        <stop offset="0" stop-color="#8fb0c9"/><stop offset="0.12" stop-color="#3f6a2c"/><stop offset="1" stop-color="#2f5524"/>
      </linearGradient>
      <linearGradient id="tone-winter" x1="0" y1="0" x2="0" y2="1">
        <stop offset="0" stop-color="#c79ab4"/><stop offset="0.55" stop-color="#6a4a3e"/><stop offset="1" stop-color="#e6e9f0"/>
      </linearGradient>
      <linearGradient id="tone-living" x1="0" y1="0" x2="0" y2="1">
        <stop offset="0" stop-color="#efe8dc"/><stop offset="1" stop-color="#8b5a36"/>
      </linearGradient>
    </defs>
    <g fill="none" stroke="#c0202a" stroke-width="4" stroke-linejoin="round">
      <polygon role="img" aria-label="Photo of a bright living room with a fireplace and chandelier" fill="url(#tone-interior)" points="100,52 268,52 330,180 268,310 100,310 38,180"/>
      <polygon role="img" aria-label="Photo of a backyard pool with a pool house and gardens" fill="url(#tone-pool)" points="330,183 490,183 553,312 490,440 330,440 268,312"/>
      <polygon role="img" aria-label="Aerial photo of a house surrounded by forest" fill="url(#tone-aerial)" points="100,313 268,313 330,440 268,567 100,567 38,440"/>
      <polygon role="img" aria-label="Photo of a brick house in winter snow at dusk" fill="url(#tone-winter)" points="685,191 785,191 833,277 785,362 685,362 637,277"/>
      <polygon role="img" aria-label="Sample floor plan drawing" fill="#f4f4f4" points="838,279 940,279 988,364 940,449 838,449 790,364"/>
      <polygon role="img" aria-label="Photo of a living room with hardwood floors" fill="url(#tone-living)" points="685,366 785,366 833,450 785,535 685,535 637,450"/>
    </g>
  </svg>

  <div class="page-divider"></div>

  <!-- Cover page -->
  <p class="tagline">Presentation is everything.</p>
  <div class="brand brand--cover">
    <span class="brand-mark"></span>
    <span class="brand-name">Open House Imaging</span>
  </div>
  <div class="services-band">Photography | Floor Plans | Video Tours</div>
  <p class="cover-contact">www.OpenHouseImaging.com<br>555-014-2290</p>

  <!-- Price page -->
  <h2 class="section-title title-packages">PACKAGE PRICING:</h2>
  <ul class="price-list list-packages">
    <li>Silver Package: 15 Photos + Floor Plan (3,500 sqft) - $225</li>
    <li>Gold Package: 25 Photos + Floor Plan (4,500 sqft) - $300</li>
    <li>Platinum Package: 35 Photos + Floor Plan (5,500 sqft) - $375</li>
  </ul>

  <h2 class="section-title title-floorplans">FLOOR PLANS</h2>
  <ul class="price-list list-floorplans">
    <li>Floor Plan (3,500 sqft) - $150</li>
    <li>Floor Plan (4,500 sqft) - $175</li>
    <li>Floor Plan (5,500 sqft) - $200</li>
    <li>*$25 per additional 500sqft</li>
    <li>**Complex floor plans are priced individually regardless of sqft</li>
  </ul>

  <h2 class="section-title title-photo">PHOTOGRAPHY ONLY</h2>
  <ul class="price-list list-photo">
    <li>15 Photo Bundle: $100</li>
    <li>25 Photo Bundle: $150</li>
    <li>35 Photo Bundle: $200</li>
  </ul>

  <h2 class="section-title title-extra">ADDITIONAL SERVICES</h2>
  <ul class="price-list list-extra">
    <li>Aerial Photos: 3-6 Photos - $200</li>
    <li>($75 if combined with another package)</li>
    <li>Aerial Video: (1-3 min video) - $375</li>
    <li>Branded Video Tour w/ Aerial Video: (2-4 min video of property) - $800-$1300</li>
    <li>(voiceover optional, call for details)</li>
    <li>Twilight Photos: 3-6 Photos - $225</li>
    <li>Luxury Package: $2,000 (includes all services listed)</li>
  </ul>

  <div class="booking-band"></div>
  <p class="booking-text">For more information or to book a shoot please visit our<br>website: www.OpenHouseImaging.com<br>or call Dana at 555-014-2290</p>
  <div class="brand-box">
    <div class="brand brand--back">
      <span class="brand-mark"></span>
      <span class="brand-name">Open House Imaging</span>
    </div>
  </div>
</main>
</body>
</html>
```